Property Service business needs a cool business card

Looking for an eloquent and unique business card using the logo and colours attached as uploaded files.

Target Market(s)

Body corporates, real estate agents, building managers

Industry/Entity Type

Business

Contact Information for Business Card

- Kelvo Logo
- Construction * Maintenance * Remedial

- Ned Pirrick
- Business Manager

- Ph 0417586043
- P.O Box 514 Port Belmont Vic 3185
- Email ned@kelvo.com
- Website www.kelvopropertyservices.com.au

Requirements
Must have
• Clean and fresh look, colours must be vibrant!
Nice to have
• unique features
Should not have
• Should not be overcrowded

```html
<!DOCTYPE html>
<html lang="en">
<head>
<meta charset="utf-8">
<title>Kelvo Property Services – Business Card</title>
<link rel="stylesheet" href="https://fonts.googleapis.com/css2?family=Exo+2:wght@400;500&display=swap">
<style>
  :root {
    --brand-blue: #0b4f9c;
    --brand-green: #8db51a;
    --brand-grey: #8a8c8f;
    --label-grey: #7b7d80;
    --card-white: #fbfbfb;
    --stage: #3a3b3d;
    --rule: #9a9a9a;
  }
  * { margin: 0; padding: 0; box-sizing: border-box; }
  html, body {
    width: 1200px; height: 900px; overflow: hidden;
    background: var(--stage);
    font-family: "Exo 2", Arial, sans-serif;
  }
  .canvas { position: relative; width: 1200px; height: 900px; }

  .card {
    position: absolute;
    width: 640px; height: 366px;
    overflow: hidden;
    box-shadow: 0 8px 24px rgba(0,0,0,.45);
  }

  /* Front */
  .card-front { left: 110px; top: 60px; background: var(--brand-blue); }
  .card-front .brand {
    position: absolute; left: 70px; top: 150px;
    display: flex; align-items: center; gap: 14px;
    color: #ffffff; font-size: 40px; font-weight: 500; letter-spacing: 1px; line-height: 1;
  }
  .brand-square { width: 34px; height: 34px; background: currentColor; flex: none; }
  .card-front .feature-panel {
    position: absolute; right: 0; top: 0; width: 300px; height: 366px;
  }

  /* Back */
  .card-back { left: 450px; top: 470px; background: var(--card-white); }
  .card-back .brand {
    position: absolute; right: 60px; top: 50px;
    display: flex; align-items: center; gap: 12px;
    color: var(--brand-blue); font-size: 34px; font-weight: 500; letter-spacing: 1px; line-height: 1;
  }
  .card-back .brand-square { width: 28px; height: 28px; background: var(--brand-green); }

  .address {
    position: absolute; right: 60px; top: 130px;
    font-style: normal; text-align: right;
    font-size: 16px; line-height: 20px; color: var(--brand-blue);
  }

  .person { position: absolute; left: 40px; top: 180px; color: var(--brand-blue); }
  .person-name { font-size: 22px; font-weight: 500; line-height: 26px; }
  .person-role { font-size: 16px; line-height: 20px; margin-top: 2px; }

  .divider {
    position: absolute; left: 222px; right: 60px; top: 206px;
    height: 1px; background: var(--rule);
  }

  .contact {
    position: absolute; left: 40px; top: 240px;
    list-style: none; font-size: 16px; line-height: 22px; color: var(--brand-blue);
  }
  .contact-label { display: inline-block; width: 26px; color: var(--label-grey); }

  .services-band {
    position: absolute; left: 0; right: 0; bottom: 0; height: 46px;
    background: var(--brand-green);
    display: flex; align-items: center; justify-content: center;
    color: rgba(255,255,255,.88);
    font-size: 16px; letter-spacing: 6px; text-transform: uppercase;
  }
</style>
</head>
<body>
<main class="canvas">

  <section class="card card-front" aria-label="Business card front">
    <div class="brand"><span class="brand-square"></span>Kelvo</div>
    <svg class="feature-panel" role="img" aria-label="Geometric brand graphic in green, grey and white" viewBox="0 0 300 366">
      <defs>
        <linearGradient id="panelTone" x1="0" y1="0" x2="1" y2="1">
          <stop offset="0" stop-color="#ffffff" stop-opacity=".85"/>
          <stop offset=".45" stop-color="#9a9c9f" stop-opacity=".9"/>
          <stop offset="1" stop-color="#8db51a"/>
        </linearGradient>
      </defs>
      <rect width="300" height="366" fill="url(#panelTone)"/>
    </svg>
  </section>

  <section class="card card-back" aria-label="Business card back">
    <div class="brand"><span class="brand-square"></span>Kelvo</div>

    <address class="address">P.O Box 514<br>Port Belmont<br>Vic 3185</address>

    <div class="person">
      <div class="person-name">Ned Pirrick</div>
      <div class="person-role">Business Manager</div>
    </div>

    <div class="divider"></div>

    <ul class="contact">
      <li><span class="contact-label">P</span>0417 586 043</li>
      <li><span class="contact-label">E</span>ned@kelvo.com</li>
      <li><span class="contact-label">W</span>www.kelvopropertyservices.com.au</li>
    </ul>

    <div class="services-band">Construction / Maintenance / Remedial</div>
  </section>

</main>
</body>
</html>
```